Marwick Dance Festival Association

We need a design for a pull up banner for the dance festival. The festival takes place every year and aims to encourage dancers in the local area to perform. Dancers are judged on their performance the genres include ballet, jazz, tap and hip hop.
The banner will be 850mm x 2000mm. .ai files will be required.
We have no current logo - a new logo can be included as part of the design. Please do not include the year as it is a banner we would use over several years. We are looking for bright attractive colours - preferably with a reflection of the different genres. One suggestion was to include silhouettes of the different genres (in colour) but other suggestions are welcome.

```html
<!DOCTYPE html>
<html lang="en">
<head>
<meta charset="utf-8">
<title>Marwick Dance Festival – Pull Up Banner</title>
<link rel="stylesheet" href="https://fonts.googleapis.com/css2?family=Cinzel:wght@700&family=Lobster&family=DotGothic16&family=Didact+Gothic&display=swap">
<style>
  :root {
    --white: #ffffff;
    --ink: #111111;
    --teal: #2fbf8f;
    --violet: #6a3fb8;
    --purple: #8a4fae;
    --green: #3f9a3a;
    --hot-pink: #f0306a;
    --name-pink: #ff6fd8;
    --title-crimson: #8a0d3a;
    --swoosh-blue: #7fd8ff;
    --hiphop: #ff2d2d;
    --ballet: #ffa412;
    --jazz: #3ee42a;
    --tap: #2ad0ff;
    --presents: #e8e8ff;
    --dark-badge: #161616;
  }
  * { margin: 0; padding: 0; box-sizing: border-box; }
  html, body { width: 1200px; height: 900px; overflow: hidden; background: var(--white); }
  .canvas { position: relative; width: 1200px; height: 900px; }

  .banner {
    position: absolute; left: 0; top: 0; width: 1200px; height: 510px; overflow: hidden;
    background:
      radial-gradient(ellipse 420px 320px at 230px 220px, var(--teal), transparent 75%),
      radial-gradient(ellipse 420px 300px at 560px 200px, var(--violet), transparent 75%),
      radial-gradient(ellipse 380px 320px at 1120px 80px, var(--green), transparent 75%),
      linear-gradient(180deg, var(--purple) 0%, #7a5c8f 55%, var(--hot-pink) 80%);
  }
  .badge { position: absolute; left: 244px; top: 44px; width: 136px; height: 136px;
    border-radius: 50%; background: var(--dark-badge); }
  .association {
    position: absolute; left: 414px; top: 80px;
    font-family: "Cinzel", serif; font-weight: 700; font-size: 33px;
    color: var(--name-pink); white-space: nowrap; letter-spacing: 0.5px;
  }
  .swoosh { position: absolute; left: 405px; top: 120px; }
  .presents {
    position: absolute; left: 0; width: 1200px; top: 180px; text-align: center;
    font-family: "DotGothic16", sans-serif; font-size: 24px; color: var(--presents);
    letter-spacing: 2px;
  }
  .festival-title {
    position: absolute; left: 0; width: 1200px; top: 244px; text-align: center;
    font-family: "Lobster", cursive; font-size: 76px; color: var(--title-crimson);
    text-shadow: -2px -2px 0 var(--white), 2px -2px 0 var(--white), -2px 2px 0 var(--white),
                 2px 2px 0 var(--white), 4px 6px 6px rgba(0,0,0,.7);
  }
  .crowd {
    position: absolute; left: 0; top: 380px; width: 1200px; height: 130px;
    background: linear-gradient(180deg, rgba(0,0,0,0) 0%, rgba(0,0,0,.85) 30%, var(--ink) 55%);
  }
  .genres { position: absolute; top: 464px; left: 0; width: 1200px; height: 40px;
    font-family: "DotGothic16", sans-serif; font-size: 30px; letter-spacing: 3px; }
  .genre { position: absolute; top: 0; }
  .genre--hiphop { left: 245px; color: var(--hiphop); }
  .genre--ballet { left: 487px; color: var(--ballet); }
  .genre--jazz { left: 705px; color: var(--jazz); }
  .genre--tap { left: 882px; color: var(--tap); }

  .detail-loupe { position: absolute; left: 17px; top: 529px; }
  .quality-note {
    position: absolute; left: 385px; width: 800px; top: 596px; text-align: center;
    font-family: "Didact Gothic", sans-serif; font-size: 40px; line-height: 61px; color: var(--ink);
  }
</style>
</head>
<body>
<div class="canvas">
  <section class="banner">
    <div class="badge"></div>
    <div class="association">Marwick Dance Festival Association</div>
    <svg class="swoosh" width="550" height="30" viewBox="0 0 550 30">
      <path d="M6 24 Q270 4 545 8 Q270 16 6 26 Z" fill="var(--swoosh-blue)"/>
    </svg>
    <div class="presents">PRESENTS</div>
    <h1 class="festival-title">Marwick Dance Festival</h1>
    <div class="crowd" role="img" aria-label="Silhouette of a cheering crowd with raised hands"></div>
    <div class="genres">
      <span class="genre genre--hiphop">HIP HOP</span>
      <span class="genre genre--ballet">BALLET</span>
      <span class="genre genre--jazz">JAZZ</span>
      <span class="genre genre--tap">TAP</span>
    </div>
  </section>

  <svg class="detail-loupe" width="358" height="358" viewBox="0 0 358 358">
    <defs>
      <clipPath id="loupe-clip"><circle cx="179" cy="179" r="178"/></clipPath>
      <linearGradient id="loupe-fill" x1="0" y1="0" x2="1" y2="1">
        <stop offset="0" stop-color="#4a4fbf"/>
        <stop offset="1" stop-color="#7a5ad0"/>
      </linearGradient>
    </defs>
    <g clip-path="url(#loupe-clip)">
      <rect width="358" height="358" fill="url(#loupe-fill)" role="img" aria-label="Enlarged fine line texture of the banner background"/>
      <text x="-20" y="92" font-family="Cinzel, serif" font-weight="700" font-size="58" fill="var(--name-pink)">ARWICK DANCE</text>
      <path d="M0 148 Q200 128 358 128 L358 136 Q200 140 0 156 Z" fill="var(--white)"/>
      <path d="M0 156 Q200 140 358 136 L358 140 Q200 146 0 160 Z" fill="var(--swoosh-blue)"/>
      <text x="184" y="276" font-family="DotGothic16, sans-serif" font-size="48" fill="var(--white)" letter-spacing="3">PRESENTS</text>
    </g>
  </svg>

  <p class="quality-note">High Quality<br>You will see the effects after printing</p>
</div>
</body>
</html>
```